A website for Medical Services to treat incontinence with a non-invasive product

We need to build a website to generate and convert new clients to schedule either treatment or book consultation (The device's name is KVR TONARIX). Here are the reference sites for information only: (Please do not use the same style as this is the style we desperately want to change)
http://www.pelvoracare.example/tonarix-for-incontinence/
https://vormidaspa.example/2018/04/13/urinary-incontinence/
https://vormidaspa.example/non-invasive-lasers/female-incontinence/
http://www.drquaven.example/services/wellness-services/sexual-health/kvr-tonarix-urinary-incontinence-houston/

This is the vendor site:
https://corvanthmed.example/

Target Market(s)

The targeted audience is mostly women between 30 - 75, suffering from stress incontinence due to childbirth and many other age-related conditions.

Industry/Entity Type

Health And Wellness

Number of Pages Required

4 page

Font styles to use
Sans Serif

Colors

Designer to choose colors to be used in the design.

Requirements
Must have
• How it works, How is it different from traditional invasive measures, What other people say about the treatment, video testimonials, FAQs, contact us, Book Appointment, latest promotions. maps, social media links
Nice to have
• The experienced urologist profile, office surroundings/interior, Reviews, number strips

```html
<!DOCTYPE html>
<html lang="en">
<head>
<meta charset="utf-8">
<title>KVR TONARIX – Incontinence Treatment</title>
<link href="https://fonts.googleapis.com/css2?family=Open+Sans:wght@300;400;600;700&display=swap" rel="stylesheet">
<style>
:root{
  --peach:#f6c2a7;
  --peach-deep:#f3b394;
  --brown:#5e4a3f;
  --text:#555;
  --heading:#3a3a3a;
  --grey-bg:#f2f2f2;
  --footer:#3e3634;
  --white:#fff;
}
*{margin:0;padding:0;box-sizing:border-box}
html,body{width:1200px;height:3965px;overflow:hidden}
body{position:relative;font-family:"Open Sans",Arial,sans-serif;color:var(--text);background:var(--white)}
.abs{position:absolute}
.btn{position:absolute;display:flex;align-items:center;justify-content:center;background:var(--peach);color:var(--white);font-size:13px;font-weight:700;letter-spacing:.5px;text-transform:uppercase;border-radius:3px;box-shadow:0 3px 8px rgba(0,0,0,.12)}
/* top bar */
.topbar{top:0;left:0;width:1200px;height:32px;background:var(--peach);color:var(--white);font-size:12px}
.topbar .social{left:85px;top:10px;display:flex;gap:8px}
.topbar .social span{width:11px;height:11px;border-radius:50%;background:var(--white);opacity:.9}
.topbar .call{left:0;width:1200px;top:8px;text-align:center}
.topbar .login{right:85px;top:8px;font-weight:600}
/* hero */
.hero{top:32px;left:0;width:1200px;height:603px;background:linear-gradient(180deg,#f4f1e6 0%,#f0e8c8 50%,#d8b560 82%,#b88a34 100%)}
.hero-photo{top:0;left:520px;width:680px;height:603px;background:radial-gradient(ellipse at 60% 40%,rgba(255,255,255,.55),rgba(255,255,255,0) 65%)}
.logo{font-weight:700;letter-spacing:1px;font-size:22px;color:var(--brown)}
.hero .logo{left:85px;top:25px}
.nav{top:28px;left:372px;display:flex;gap:31px;font-size:13px;color:var(--brown)}
.nav .active{font-weight:700}
.hero .book{left:953px;top:21px;width:162px;height:34px;font-size:11px;text-transform:none;font-weight:600}
.hero-title{left:85px;top:188px;font-size:44px;font-weight:300;line-height:52px;color:var(--white);text-shadow:0 1px 2px rgba(0,0,0,.08)}
.hero-title b{font-weight:700;color:var(--brown);letter-spacing:1px;text-shadow:none}
.hero-title .lead{color:#8a7a66}
.hero .learn{left:88px;top:364px;width:150px;height:45px;border:2px solid var(--brown);color:var(--brown);font-size:13px;display:flex;align-items:center;justify-content:center;text-transform:uppercase;font-weight:600}
/* about */
.about{top:597px;left:87px;width:1026px;height:275px;background:var(--white);box-shadow:0 4px 18px rgba(0,0,0,.12);text-align:center}
.about h2{margin-top:46px;font-size:38px;font-weight:300;color:var(--brown)}
.about h2 b{font-weight:600}
.about p{width:780px;margin:30px auto 0;font-size:13px;line-height:21px}
/* how it works */
.section-title{position:absolute;left:0;width:1200px;text-align:center;font-size:38px;font-weight:600;color:var(--heading)}
.how-sub{top:980px;left:0;width:1200px;text-align:center;font-size:16px;color:var(--text)}
.step{width:300px;text-align:center}
.step .disc{width:170px;height:170px;margin:0 auto;border-radius:50%;border:2px solid #e9e0da;background:radial-gradient(circle at 50% 55%,#f7ddd0 0%,#f3e9e4 60%,#fbf8f6 100%)}
.step h3{margin-top:24px;font-size:20px;font-weight:400;color:#c99479;letter-spacing:1px}
.step p{margin-top:6px;font-size:14px;line-height:21px}
.arrow-link{top:1103px}
/* dark band */
.band{top:1377px;left:0;width:1200px;height:465px;background:linear-gradient(90deg,#2b2522 0%,#3a3230 50%,#6a574d 78%,#4b3e38 100%)}
.band h2{position:absolute;top:128px;left:0;width:1200px;text-align:center;font-size:36px;font-weight:600;line-height:44px;color:var(--white)}
.band p{position:absolute;top:218px;left:320px;width:560px;text-align:center;font-size:14px;line-height:22px;color:#ddd}
.band .btn{left:526px;top:287px;width:148px;height:40px}
/* testimonials */
.testi-title{left:128px;top:1935px;width:420px;text-align:center;font-size:36px;font-weight:600;color:var(--heading)}
.quote{left:312px;top:1985px;font-size:60px;line-height:50px;color:var(--heading);font-weight:700}
.testi-text{left:98px;top:2032px;width:480px;text-align:center;font-size:14px;line-height:22px}
.testi-name{left:98px;top:2113px;width:480px;text-align:center;font-size:13px;font-weight:700;letter-spacing:1px;color:var(--heading)}
.testi-rule{left:304px;top:2140px;width:68px;height:2px;background:var(--heading)}
.video{left:616px;top:1901px;width:497px;height:276px;background:linear-gradient(120deg,#ddd3ca,#cbbdb0 60%,#e4dcd4)}
.video svg{position:absolute;left:213px;top:103px}
.slider-arrow{top:2020px}
/* urologist */
.uro-photo{left:95px;top:2247px;width:476px;height:325px;background:linear-gradient(135deg,#e6eef4,#bcd0de 50%,#8ea8bb);box-shadow:0 4px 14px rgba(0,0,0,.15);border:6px solid var(--white)}
.uro-title{left:613px;top:2280px;font-size:36px;font-weight:400;color:var(--heading)}
.uro-text{left:613px;top:2343px;width:410px;font-size:14px;line-height:22px}
.uro-btn{left:613px;top:2483px;width:148px;height:40px}
/* faq */
.faq-bg{top:2604px;left:0;width:1200px;height:278px;background:var(--grey-bg)}
.faq{top:2648px;left:87px;width:1026px;height:452px;background:var(--white);box-shadow:0 4px 18px rgba(0,0,0,.1)}
.faq h2{position:absolute;top:46px;left:0;width:1026px;text-align:center;font-size:38px;font-weight:400;color:#666}
.faq-item{position:absolute;left:88px;width:850px;height:46px;border:1px solid #e4e4e4;font-size:13px;font-weight:600;color:#888;padding:0 20px;display:flex;align-items:center;justify-content:space-between}
.faq-item.open{background:var(--peach);border-color:var(--peach);color:var(--white)}
.faq-answer{position:absolute;left:88px;top:159px;width:850px;height:70px;background:#f3f3f3;padding:12px 20px;font-size:13px;line-height:21px}
/* promotions */
.promo-title{top:3148px}
.card{top:3227px;width:500px;height:251px;background:var(--white);box-shadow:0 3px 14px rgba(0,0,0,.13)}
.card .pic{position:absolute;left:16px;top:18px;width:468px;height:137px}
.card h4{position:absolute;left:16px;top:170px;font-size:17px;font-weight:700;color:var(--heading)}
.card p{position:absolute;left:16px;top:196px;width:460px;font-size:13px;line-height:20px}
.promo-btn{left:526px;top:3522px;width:148px;height:40px}
/* footer */
.footer{top:3629px;left:0;width:1200px;height:291px;background:var(--footer);color:#e6e1de}
.footer .logo{position:absolute;left:87px;top:40px;color:var(--white)}
.contact-list{position:absolute;left:87px;top:92px;font-size:13px;line-height:20px}
.contact-list li{list-style:none;display:flex;gap:12px;margin-bottom:14px}
.contact-list svg{flex:none;margin-top:3px}
.footer h5{position:absolute;top:38px;font-size:20px;font-weight:600;color:var(--white)}
.quick{position:absolute;left:526px;top:86px;list-style:none;font-size:13px;line-height:31px}
.socials{position:absolute;left:875px;top:94px;display:flex;gap:7px}
.socials span{width:33px;height:33px;background:#d99b7b;border-radius:2px}
.footer .btn{left:877px;top:170px;width:162px;height:34px;font-size:11px;text-transform:none;font-weight:600}
.bottombar{top:3920px;left:0;width:1200px;height:45px;background:var(--peach);color:var(--white);font-size:12px;text-align:center;line-height:45px}
</style>
</head>
<body>

<div class="abs topbar">
  <div class="abs social"><span></span><span></span><span></span><span></span><span></span><span></span></div>
  <div class="abs call">Call us : (000) -000-000-000</div>
  <div class="abs login">Login / Register</div>
</div>

<header class="abs hero">
  <div class="abs hero-photo" role="img" aria-label="Photo of a woman leaping joyfully in a sunlit golden meadow"></div>
  <div class="abs logo">KVR TONARIX</div>
  <nav class="abs nav"><span class="active">Home</span><span>About Us</span><span>Urologist</span><span>Treatment</span><span>Consultation</span><span>Contact Us</span></nav>
  <div class="btn book">&#9635;&nbsp; Book an Appointment</div>
  <h1 class="abs hero-title"><span class="lead">Make Your Life Healthy<br>and Wellness to say<br>No to </span><b>INCONTINENCE</b></h1>
  <div class="abs learn">Learn More</div>
</header>

<section class="abs about">
  <h2>About <b>KVR TONARIX</b></h2>
  <p>Lorem Ipsum is simply dummy text of the printing and typesetting industry. Lorem Ipsum has been the industry's standard dummy text ever since the 1500s, when an unknown printer took a galley of type and scrambled it to make a type specimen book. It has survived not only five centuries, but also the leap into electronic typesetting, remaining essentially unchanged.</p>
</section>

<h2 class="section-title" style="top:918px">How it works</h2>
<p class="abs how-sub">Body Aging, Childbirth, and Menopause Can Lead to Incontinence</p>

<div class="abs step" style="left:98px;top:1036px">
  <div class="disc" role="img" aria-label="Diagram of weakened pelvic floor muscles before treatment"></div>
  <h3>BEFORE</h3>
  <p>Pelvic floor muscles insufficiently support pelvic organs and affect bladder control.</p>
</div>
<div class="abs step" style="left:450px;top:1036px">
  <div class="disc" role="img" aria-label="Diagram of pelvic floor muscles being stimulated during treatment"></div>
  <h3>TREATMENT</h3>
  <p>KVR TONARIX effectively stimulates pelvic floor muscles with thousands of supramaximal contractions.</p>
</div>
<div class="abs step" style="left:801px;top:1036px">
  <div class="disc" role="img" aria-label="Diagram of strengthened pelvic floor muscles after treatment"></div>
  <h3>AFTER</h3>
  <p>Stimulation leads to regained control over pelvic floor muscles and bladder.</p>
</div>
<svg class="abs arrow-link" style="left:396px" width="56" height="12" viewBox="0 0 56 12"><line x1="0" y1="6" x2="38" y2="6" stroke="#f0a98a" stroke-width="2" stroke-dasharray="3 3"/><path d="M40 2l4 4-4 4M47 2l4 4-4 4" fill="none" stroke="#f0a98a" stroke-width="1.5"/></svg>
<svg class="abs arrow-link" style="left:747px" width="56" height="12" viewBox="0 0 56 12"><line x1="0" y1="6" x2="38" y2="6" stroke="#f0a98a" stroke-width="2" stroke-dasharray="3 3"/><path d="M40 2l4 4-4 4M47 2l4 4-4 4" fill="none" stroke="#f0a98a" stroke-width="1.5"/></svg>

<section class="abs band" role="img" aria-label="Dark background photo of a smiling woman on the right">
  <h2>How is it different from traditional<br>invasive measures</h2>
  <p>Lorem Ipsum is simply dummy text of the printing and typesetting industry. Lorem Ipsum has been the industry's standard dummy text ever since the 1500s.</p>
  <div class="btn">View Profiles</div>
</section>

<svg class="abs slider-arrow" style="left:42px" width="14" height="36" viewBox="0 0 14 36"><path d="M12 2L2 18l10 16" fill="none" stroke="#999" stroke-width="2"/></svg>
<svg class="abs slider-arrow" style="left:1146px" width="14" height="36" viewBox="0 0 14 36"><path d="M2 2l10 16-10 16" fill="none" stroke="#999" stroke-width="2"/></svg>
<h2 class="abs testi-title">Testimonials</h2>
<div class="abs quote">&ldquo;</div>
<p class="abs testi-text">Lorem Ipsum is simply dummy text of the printing and typesetting industry. Lorem Ipsum has been the industry's standard dummy text ever since the 1500s.</p>
<div class="abs testi-name">JOHN DOE</div>
<div class="abs testi-rule"></div>
<div class="abs video" role="img" aria-label="Video testimonial of a patient beside the treatment chair">
  <svg width="72" height="72" viewBox="0 0 72 72"><circle cx="36" cy="36" r="33" fill="none" stroke="#fff" stroke-width="3"/><path d="M28 22l22 14-22 14z" fill="#fff"/></svg>
</div>

<div class="abs uro-photo" role="img" aria-label="Photo of a urologist explaining a scan on a monitor to a patient"></div>
<h2 class="abs uro-title">Urologist</h2>
<p class="abs uro-text">Lorem Ipsum is simply dummy text of the printing and typesetting industry. Lorem Ipsum has been the industry's standard dummy text ever since the 1500s, when an unknown printer took a galley of type and scrambled it to make a type specimen book. It has survived not only five centuriesunchanged.</p>
<div class="btn uro-btn">View Profiles</div>

<div class="abs faq-bg"></div>
<section class="abs faq">
  <h2>FAQs</h2>
  <div class="faq-item open" style="top:117px">Lorem Ipsum is simply dummy text of the printing and typesetting industry ? <span>&#8963;</span></div>
  <div class="faq-answer">Lorem Ipsum is simply dummy text of the printing and typesetting industry. Lorem Ipsum has been the industry's standard dummy text ever since the 1500s.</div>
  <div class="faq-item" style="top:238px">Lorem Ipsum is simply dummy text of the printing and typesetting industry ? <span>&#8964;</span></div>
  <div class="faq-item" style="top:296px">Lorem Ipsum is simply dummy text of the printing and typesetting industry ? <span>&#8964;</span></div>
  <div class="faq-item" style="top:354px">Lorem Ipsum is simply dummy text of the printing and typesetting industry ? <span>&#8964;</span></div>
</section>

<h2 class="section-title promo-title" style="font-weight:400">Latest Promotions</h2>
<article class="abs card" style="left:87px">
  <div class="pic" role="img" aria-label="Photo of a group of smiling women of different ages" style="background:linear-gradient(90deg,#d9c3b5,#b99a8c 40%,#e2a6b8 70%,#cfc3bb)"></div>
  <h4>Lorem Ipsum is simply dummy text of the</h4>
  <p>Lorem Ipsum is simply dummy text of the printing and typesetting industry ?</p>
</article>
<article class="abs card" style="left:613px">
  <div class="pic" role="img" aria-label="Photo of three laughing women in a bright room" style="background:linear-gradient(90deg,#e9e9ea,#c8b4a6 45%,#ddd3cc 75%,#eeeeee)"></div>
  <h4>Lorem Ipsum is simply dummy text of the</h4>
  <p>Lorem Ipsum is simply dummy text of the printing and typesetting industry ?</p>
</article>
<div class="btn promo-btn">View More</div>

<footer class="abs footer">
  <div class="logo">KVR TONARIX</div>
  <ul class="contact-list">
    <li><svg width="14" height="16" viewBox="0 0 14 16"><path d="M7 1a5 5 0 0 1 5 5c0 4-5 9-5 9S2 10 2 6a5 5 0 0 1 5-5z" fill="none" stroke="#e6e1de" stroke-width="1.4"/><circle cx="7" cy="6" r="1.8" fill="#e6e1de"/></svg><span>Lorem Ipsum is simply dummy<br>text of the printing and typesetting</span></li>
    <li><svg width="14" height="14" viewBox="0 0 14 14"><path d="M3 1l2 3-1.5 1.5a8 8 0 0 0 5 5L10 9l3 2-1 2c-6 0-11-5-11-11z" fill="none" stroke="#e6e1de" stroke-width="1.3"/></svg><span>000 - 0000 - 0000</span></li>
    <li><svg width="14" height="12" viewBox="0 0 14 12"><rect x="1" y="1" width="12" height="10" fill="none" stroke="#e6e1de" stroke-width="1.3"/><path d="M1 1l6 5 6-5" fill="none" stroke="#e6e1de" stroke-width="1.3"/></svg><span>info@kvrtonarix.example</span></li>
    <li><svg width="14" height="14" viewBox="0 0 14 14"><circle cx="7" cy="7" r="6" fill="none" stroke="#e6e1de" stroke-width="1.3"/><path d="M1 7h12M7 1c-3 3-3 9 0 12M7 1c3 3 3 9 0 12" fill="none" stroke="#e6e1de" stroke-width="1.1"/></svg><span>www.kvrtonarix.example</span></li>
  </ul>
  <h5 style="left:526px">Quick Links</h5>
  <ul class="quick"><li>Home</li><li>About us</li><li>Urologist</li><li>Treatment</li><li>Consultation</li><li>Contact Us</li></ul>
  <h5 style="left:875px">Follow Us</h5>
  <div class="socials"><span></span><span></span><span></span><span></span><span></span><span></span></div>
  <div class="btn">&#9635;&nbsp; Book an Appointment</div>
</footer>
<div class="abs bottombar">© 2018 KVR TONARIX &nbsp;|&nbsp; Terms of use &nbsp;|&nbsp; Privacy Statement</div>

</body>
</html>
```